Need design for an App.

The app in question is related to security and crime events with real time feed, engagement with friends and posting pictures, we want a sleak, minimal style. There are 11 or 12 screens to be made. We are adding video file as suggestion. We are not sure about colors so we accept suggestions. We are also adding the logo.

Reason: Just giving more time to designers. Thanks.

Industry/Entity Type

Security

Font styles to use
Sans Serif

Requirements
Must have
• The app must have a Login view; a new user view (with nickname, email and pass); a retrieve pass view; a menu view with options for alert configuration, send emergency alert and send report, a feed view with the most popular reports (3 worldwide at the top and near reports after), a profile view with avatar and personal reports, a send emergency alert view with a camera view; a configuration view when the user can put up to 5 contacts to send the alert to them;a send report view with camera and options to configure the camera; a edit report view where the user can see the 3 photos he will update and add a comment of those photos.
Nice to have
• Check the files we are open minds
Should not have
• old design

```html
<!DOCTYPE html>
<html lang="en">
<head>
<meta charset="utf-8">
<title>Vigilo — Sign In and Sign Up Screens</title>
<link rel="stylesheet" href="https://fonts.googleapis.com/css2?family=Roboto:wght@300;400;500&display=swap">
<style>
  :root {
    --canvas-bg: #dcd6e8;
    --shadow-start: #8c8896;
    --shadow-end: #b9b3c6;
    --title-ink: #2b2b2e;
    --screen-red: #c41e3a;
    --screen-red-deep: #9d182d;
    --ink-light: #ffffff;
    --field-line: rgba(255, 255, 255, 0.45);
    --field-text: rgba(255, 255, 255, 0.88);
  }
  * { box-sizing: border-box; margin: 0; padding: 0; }
  html, body { width: 1200px; height: 1000px; overflow: hidden; }
  body {
    position: relative;
    background: var(--canvas-bg);
    font-family: "Roboto", "Helvetica Neue", Arial, sans-serif;
    color: var(--ink-light);
  }
  .long-shadows { position: absolute; inset: 0; width: 1200px; height: 1000px; }

  .screen-title {
    position: absolute;
    top: 31px;
    width: 480px;
    text-align: center;
    font-size: 42px;
    font-weight: 300;
    color: var(--title-ink);
    letter-spacing: 0.3px;
  }
  .screen-title--signin { left: 106px; }
  .screen-title--signup { left: 619px; }

  .phone-screen {
    position: absolute;
    top: 119px;
    width: 480px;
    height: 851px;
    background: var(--screen-red);
    overflow: hidden;
  }
  .phone-screen--signin { left: 106px; }
  .phone-screen--signup { left: 619px; }

  .status-bar {
    position: absolute;
    top: 0; left: 0; right: 0;
    height: 32px;
    font-size: 17px;
    font-weight: 400;
  }
  .status-bar__left {
    position: absolute; left: 10px; top: 6px;
    display: flex; align-items: center; gap: 6px;
  }
  .status-bar__time {
    position: absolute; left: 0; right: 0; top: 6px;
    text-align: center;
  }
  .status-bar__right {
    position: absolute; right: 8px; top: 6px;
    display: flex; align-items: center; gap: 6px;
  }

  .brand {
    position: absolute;
    left: 0; right: 0;
    top: 122px;
    text-align: center;
  }
  .brand__dot {
    display: block;
    width: 58px; height: 58px;
    margin: 0 auto;
    border-radius: 50%;
    background: var(--ink-light);
  }
  .brand__name {
    display: block;
    margin-top: 62px;
    font-size: 48px;
    font-weight: 400;
    line-height: 1;
    letter-spacing: -0.5px;
  }

  .avatar-placeholder {
    position: absolute;
    left: 168px; top: 99px;
    width: 144px; height: 144px;
  }

  .form-field {
    position: absolute;
    left: 54px;
    width: 372px;
    height: 52px;
    padding-top: 2px;
    line-height: 26px;
    text-align: center;
    font-size: 23px;
    font-weight: 300;
    color: var(--field-text);
  }
  .form-field--lined { border-bottom: 1.5px solid var(--field-line); }
  .form-field--fullname { top: 329px; }
  .form-field--email { top: 404px; }
  .form-field--password { top: 481px; height: 30px; padding-top: 9px; }
  .password-dots { display: flex; justify-content: center; gap: 4px; }
  .password-dots span {
    width: 9px; height: 9px; border-radius: 50%;
    background: var(--field-text);
  }

  .primary-button {
    position: absolute;
    left: 54px; top: 556px;
    width: 372px; height: 60px;
    border-radius: 30px;
    background: var(--screen-red-deep);
    text-align: center;
    line-height: 57px;
    font-size: 24px;
    font-weight: 400;
  }

  .signin-footer {
    position: absolute;
    left: 0; right: 0; bottom: 20px;
    height: 38px;
    font-size: 18px;
  }
  .signin-footer__forgot { position: absolute; left: 27px; top: 8px; font-weight: 400; letter-spacing: 0.2px; }
  .signin-footer__divider {
    position: absolute; left: 240px; top: 0;
    width: 1px; height: 38px;
    background: var(--field-line);
  }
  .signin-footer__create {
    position: absolute; right: 25px; top: 8px;
    font-weight: 500;
    letter-spacing: 0.4px;
    text-decoration: underline;
    text-underline-offset: 3px;
  }

  .cancel-bar {
    position: absolute;
    left: 0; right: 0; bottom: 0;
    height: 59px;
    background: var(--screen-red-deep);
    text-align: center;
    line-height: 60px;
    font-size: 24px;
  }
</style>
</head>
<body>

<svg class="long-shadows" viewBox="0 0 1200 1000" aria-hidden="true">
  <defs>
    <linearGradient id="shadow-fade" x1="0" y1="0" x2="1" y2="1">
      <stop offset="0" stop-color="var(--shadow-start)" stop-opacity="0.9"/>
      <stop offset="1" stop-color="var(--shadow-end)" stop-opacity="0.7"/>
    </linearGradient>
  </defs>
  <polygon fill="url(#shadow-fade)" points="586,119 1586,1119 1106,1970 106,970"/>
  <polygon fill="url(#shadow-fade)" points="1099,119 2099,1119 1619,1970 619,970"/>
</svg>

<h2 class="screen-title screen-title--signin">Splash + Sign In Screen</h2>
<h2 class="screen-title screen-title--signup">Sign Up Screen</h2>

<section class="phone-screen phone-screen--signin">
  <div class="status-bar">
    <div class="status-bar__left">
      <svg width="50" height="10" viewBox="0 0 50 10" aria-hidden="true">
        <circle cx="5" cy="5" r="4.2" fill="#fff"/>
        <circle cx="15" cy="5" r="4.2" fill="#fff"/>
        <circle cx="25" cy="5" r="4.2" fill="#fff"/>
        <circle cx="35" cy="5" r="3.6" fill="none" stroke="#fff" stroke-width="1.1"/>
        <circle cx="45" cy="5" r="3.6" fill="none" stroke="#fff" stroke-width="1.1"/>
      </svg>
      <span>Nexcell</span>
      <svg width="18" height="14" viewBox="0 0 18 14" aria-hidden="true">
        <path d="M1 5 A11 11 0 0 1 17 5" fill="none" stroke="#fff" stroke-width="2"/>
        <path d="M4 8 A7 7 0 0 1 14 8" fill="none" stroke="#fff" stroke-width="2"/>
        <circle cx="9" cy="11.5" r="2" fill="#fff"/>
      </svg>
    </div>
    <div class="status-bar__time">4:21 PM</div>
    <div class="status-bar__right">
      <span>100%</span>
      <svg width="36" height="14" viewBox="0 0 36 14" aria-hidden="true">
        <rect x="0.75" y="0.75" width="31.5" height="12.5" rx="2.5" fill="none" stroke="#fff" stroke-width="1.2"/>
        <rect x="2.5" y="2.5" width="28" height="9" rx="1.2" fill="#fff"/>
        <rect x="33" y="4.5" width="2" height="5" rx="1" fill="#fff"/>
      </svg>
    </div>
  </div>

  <div class="brand">
    <span class="brand__dot"></span>
    <span class="brand__name">Vigilo</span>
  </div>

  <div class="form-field form-field--lined form-field--email">email address</div>
  <div class="form-field form-field--password" aria-label="password">
    <div class="password-dots"><span></span><span></span><span></span><span></span><span></span><span></span><span></span><span></span></div>
  </div>

  <div class="primary-button">Sign in</div>

  <div class="signin-footer">
    <span class="signin-footer__forgot">Forgot password?</span>
    <span class="signin-footer__divider"></span>
    <span class="signin-footer__create">Create an Account</span>
  </div>
</section>

<section class="phone-screen phone-screen--signup">
  <div class="status-bar">
    <div class="status-bar__left">
      <svg width="50" height="10" viewBox="0 0 50 10" aria-hidden="true">
        <circle cx="5" cy="5" r="4.2" fill="#fff"/>
        <circle cx="15" cy="5" r="4.2" fill="#fff"/>
        <circle cx="25" cy="5" r="4.2" fill="#fff"/>
        <circle cx="35" cy="5" r="3.6" fill="none" stroke="#fff" stroke-width="1.1"/>
        <circle cx="45" cy="5" r="3.6" fill="none" stroke="#fff" stroke-width="1.1"/>
      </svg>
      <span>Nexcell</span>
      <svg width="18" height="14" viewBox="0 0 18 14" aria-hidden="true">
        <path d="M1 5 A11 11 0 0 1 17 5" fill="none" stroke="#fff" stroke-width="2"/>
        <path d="M4 8 A7 7 0 0 1 14 8" fill="none" stroke="#fff" stroke-width="2"/>
        <circle cx="9" cy="11.5" r="2" fill="#fff"/>
      </svg>
    </div>
    <div class="status-bar__time">4:21 PM</div>
    <div class="status-bar__right">
      <span>100%</span>
      <svg width="36" height="14" viewBox="0 0 36 14" aria-hidden="true">
        <rect x="0.75" y="0.75" width="31.5" height="12.5" rx="2.5" fill="none" stroke="#fff" stroke-width="1.2"/>
        <rect x="2.5" y="2.5" width="28" height="9" rx="1.2" fill="#fff"/>
        <rect x="33" y="4.5" width="2" height="5" rx="1" fill="#fff"/>
      </svg>
    </div>
  </div>

  <svg class="avatar-placeholder" viewBox="0 0 144 144" aria-label="Profile photo placeholder" role="img">
    <defs>
      <clipPath id="avatar-clip"><circle cx="72" cy="72" r="66"/></clipPath>
    </defs>
    <circle cx="72" cy="72" r="68.5" fill="var(--screen-red-deep)" stroke="#fff" stroke-width="6"/>
    <g clip-path="url(#avatar-clip)" fill="#fff">
      <ellipse cx="72" cy="57" rx="21" ry="24"/>
      <rect x="29" y="90" width="86" height="70" rx="22"/>
    </g>
  </svg>

  <div class="form-field form-field--lined form-field--fullname">full name</div>
  <div class="form-field form-field--lined form-field--email">email address</div>
  <div class="form-field form-field--password" aria-label="password">
    <div class="password-dots"><span></span><span></span><span></span><span></span><span></span><span></span><span></span><span></span></div>
  </div>

  <div class="primary-button">Register</div>

  <div class="cancel-bar">Cancel</div>
</section>

</body>
</html>
```